Business Card Design for a Lending Business (Hard Money loans)

We need a business card for our Real Estate Lending business. We do hard Money loans for real estate investors. We have an existing logo we like, see attached. I'd like the business card to mostly include the logo colors, but a bright color pop of some sort would be nice to see also. Card should include Logo, Company Name, Company Address, Employee Name, Cell Phone, Main Phone, Email, Website

Industry/Entity Type

Finance / Lending

Contact Information for Business Card

Logo, Company Name, Company Address, Employee Name, Cell Phone, Main Phone, Email, Website

Requirements
Nice to have
• I'd like the business card to mostly include the logo colors, but a bright color pop of some sort would be nice to see also.

```html
<!DOCTYPE html>
<html lang="en">
<head>
<meta charset="utf-8">
<title>Harborline Capital – Business Card</title>
<link href="https://fonts.googleapis.com/css2?family=Open+Sans:wght@400;600;700&display=swap" rel="stylesheet">
<style>
  :root {
    --navy: #283583;
    --cyan: #1ba8e0;
    --white: #ffffff;
    --ink: #3a3a3a;
    --backdrop: #e4e5e8;
  }
  * { box-sizing: border-box; margin: 0; padding: 0; }
  html, body { width: 1200px; height: 800px; overflow: hidden; }
  body {
    background: var(--backdrop);
    font-family: "Open Sans", Arial, sans-serif;
    display: flex;
    align-items: center;
    justify-content: center;
    gap: 60px;
  }
  .card {
    position: relative;
    width: 525px;
    height: 300px;
    box-shadow: 0 6px 18px rgba(0,0,0,0.15);
  }
  /* Front */
  .card--front { background: var(--navy); color: var(--white); }
  .front__web {
    position: absolute; top: 26px; left: 30px;
    font-size: 13px; letter-spacing: 3px; font-weight: 600;
  }
  .front__web .accent { color: var(--cyan); }
  .wordmark {
    position: absolute;
    display: flex; align-items: center; gap: 12px;
    font-weight: 700; letter-spacing: 3px; line-height: 1.15;
    text-transform: uppercase;
  }
  .wordmark__dot { width: 34px; height: 34px; border-radius: 50%; flex: none; }
  .card--front .wordmark { right: 40px; bottom: 44px; font-size: 24px; color: var(--white); }
  .card--front .wordmark__dot { background: var(--white); }
  /* Back */
  .card--back { background: var(--white); color: var(--ink); }
  .person { position: absolute; top: 26px; left: 30px; font-size: 12.5px; line-height: 1.55; }
  .person__name { color: var(--cyan); font-weight: 700; text-transform: uppercase; font-size: 14px; }
  .contact-line { display: flex; align-items: center; gap: 6px; }
  .icon { width: 12px; height: 12px; flex: none; }
  .card--back .wordmark { left: 150px; top: 118px; font-size: 26px; color: var(--navy); }
  .card--back .wordmark__dot { background: var(--cyan); }
  .office {
    position: absolute; right: 28px; bottom: 22px;
    font-size: 12.5px; line-height: 1.6; text-align: right;
  }
  .office .contact-line { justify-content: flex-end; }
</style>
</head>
<body>
  <section class="card card--front" aria-label="Card front">
    <p class="front__web">www.<span class="accent">harborlinecapital</span>.com</p>
    <div class="wordmark"><span class="wordmark__dot"></span><span>Harborline<br>Capital</span></div>
  </section>

  <section class="card card--back" aria-label="Card back">
    <div class="person">
      <p class="person__name">Marcus Ellery</p>
      <p>CEO</p>
      <p class="contact-line">
        <svg class="icon" viewBox="0 0 12 12"><rect x="3" y="0.5" width="6" height="11" rx="1" fill="none" stroke="var(--navy)" stroke-width="1.2"/><circle cx="6" cy="9.6" r="0.7" fill="var(--navy)"/></svg>
        555-210-4471
      </p>
      <p class="contact-line">
        <svg class="icon" viewBox="0 0 12 12"><rect x="0.5" y="2.5" width="11" height="7" fill="var(--navy)"/><path d="M0.8 2.8 6 7 11.2 2.8" fill="none" stroke="var(--white)" stroke-width="1"/></svg>
        info@harborlinecapital.com
      </p>
    </div>

    <div class="wordmark"><span class="wordmark__dot"></span><span>Harborline<br>Capital</span></div>

    <div class="office">
      <p class="contact-line">555-318-2040
        <svg class="icon" viewBox="0 0 12 12"><path d="M2.5 1 4.5 1 5.3 3.6 4 4.6Q5 7 7.4 8L8.4 6.7 11 7.5 11 9.5Q10.5 11 9 11 1 10 1 3 1 1.5 2.5 1Z" fill="var(--navy)"/></svg>
      </p>
      <p class="contact-line">www.harborlinecapital.com
        <svg class="icon" viewBox="0 0 12 12"><circle cx="6" cy="6" r="5.3" fill="none" stroke="var(--navy)" stroke-width="1"/><ellipse cx="6" cy="6" rx="2.3" ry="5.3" fill="none" stroke="var(--navy)" stroke-width="0.8"/><path d="M0.7 6H11.3" stroke="var(--navy)" stroke-width="0.8"/></svg>
      </p>
      <p class="contact-line">1820 Alder Mill Road, Fairhaven, MD 21090
        <svg class="icon" viewBox="0 0 12 12"><path d="M6 11.5 2.3 6.2A4 4 0 1 1 9.7 6.2Z" fill="var(--navy)"/><circle cx="6" cy="4.5" r="1.4" fill="var(--white)"/></svg>
      </p>
    </div>
  </section>
</body>
</html>
```